Tarvolin - Clever Border Flow Lifting Traders

Web Design for international start-up, which is automating customs clearance processes for forwarding companies by applying a web application, which is operating with artificial intelligence and robotic process automation. Tarvolin pursues the vision of supporting forwarding companies successfully in becoming digital masters and co-creates innovative software solutions with all participants (ex- and importers of goods) along value-added chains. With intelligent/smart/digital customs clearance software or in other words, a virtual customs clearance roboter tailord to the customers needs, we are transforming businesses. The website could look like this:

https://www.krt-example.com/uk-en/index.php
or
https://sitepress-example.com/theme/marlowfield

Please use colours and designs you think would be the best fit. These websites are just here to give you an idea of how the webdesign could look like. Use the attached logo design as a basis for further web design. You can use the provided pictures, but you can also use your own ones, if you think they are better suited. But please take care, that they have a high resolution quality.

Description of Website: The website is transparent and modern. It provides seven pages such as homepage, products, web app, the about us, working at Tarvolin, News, contact us and search results page. The homepage or landing page should be filled with a short description of the company, what Tarvolin is doing, how they will support its customers and will also include a video of the provided solution. Products provide obviously information about different products and their characteristics. Web app page includes information about principles and technologies that get the software going. The about us page includes unique advantages and value propositions for customers and the contact us, as the name already says, will provide contact information and possibilities to contact us. The rest is also obvious (for additional information look up the website of KRT, priorly provided link - the page is also available in english).

If you have any questions, I am happy to answer them any time.
Updates

I have to think about the text that I want to have included into the design and hadn't have the time to compose it.

Target Market(s)

Forwarding Companies, Ex-/Importers

Industry/Entity Type

It Company

Number of Pages Required

5+ page

Requirements
Must have
• The web design should be designes according to the attached logo of Tarvolin.

```html
<!DOCTYPE html>
<html lang="en">
<head>
<meta charset="utf-8">
<title>Tarvolin – Clever Border Flow Lifting Traders</title>
<link href="https://fonts.googleapis.com/css2?family=Montserrat:wght@400;500;600;700;800&family=Poppins:wght@300;400&family=Oswald:wght@400&display=swap" rel="stylesheet">
<style>
:root{
  --red:#cb3a2d;
  --red-deep:#9b2a3a;
  --ink:#111111;
  --text:#555555;
  --muted:#777777;
  --white:#ffffff;
  --black:#000000;
  --line:#e2e2e2;
  --grad:linear-gradient(90deg,var(--red) 0%,var(--red-deep) 100%);
}
*{margin:0;padding:0;box-sizing:border-box}
html,body{width:1200px;height:2891px;overflow:hidden;background:var(--white)}
body{position:relative;font-family:'Poppins',sans-serif;color:var(--text)}
.abs{position:absolute}
.heading{font-family:'Montserrat',sans-serif;font-weight:800;color:var(--ink);text-transform:uppercase}
.accent{color:var(--red)}
.btn{position:absolute;display:flex;align-items:center;justify-content:center;border-radius:30px;background:var(--grad);color:var(--white);font-family:'Montserrat',sans-serif;font-weight:700;text-transform:uppercase;letter-spacing:.5px}

/* header */
.site-header{position:absolute;left:0;top:0;width:1200px;height:83px;background:var(--white)}
.brand{position:absolute;left:76px;top:20px;font-family:'Montserrat',sans-serif;font-weight:700;font-size:36px;color:var(--ink)}
.nav{position:absolute;top:35px;font-family:'Montserrat',sans-serif;font-size:15px;color:#333;text-transform:uppercase}
.nav.active{color:var(--red)}
.btn-login{left:1029px;top:22px;width:93px;height:41px;font-size:15px}

/* hero */
.hero{position:absolute;left:0;top:83px;width:1200px;height:594px;background:linear-gradient(110deg,#2a2622 0%,#5a3a2c 30%,#7a3a25 50%,#3a3632 75%,#2b2b2e 100%)}
.hero-title{position:absolute;left:0;top:195px;width:1200px;text-align:center;font-family:'Montserrat',sans-serif;font-weight:800;font-size:40px;line-height:47px;color:var(--white);text-transform:uppercase}
.hero-sub{position:absolute;left:0;top:297px;width:1200px;text-align:center;font-family:'Oswald',sans-serif;font-size:25px;color:var(--white)}
.btn-hero{left:502px;top:354px;width:197px;height:50px;font-size:20px}
.slider-arrow{position:absolute;top:262px;width:48px;height:48px;border:1px solid rgba(255,255,255,.6);border-radius:50%}

/* welcome */
.welcome-title{position:absolute;left:80px;top:737px;font-size:42px;line-height:47px}
.welcome-copy{position:absolute;left:79px;width:500px;font-size:13.5px;line-height:27px;color:var(--text)}
.btn-learn{left:77px;top:1048px;width:187px;height:52px;font-size:19px}
.welcome-frame{position:absolute;left:781px;top:745px;width:341px;height:312px;background:linear-gradient(120deg,var(--red),var(--red-deep))}
.welcome-media{position:absolute;left:718px;top:786px;width:365px;height:312px;background:linear-gradient(90deg,#0b0f1a 0%,#0d2550 45%,#7d8a98 80%,#3a4450 100%)}
.play{position:absolute;left:690px;top:915px;width:60px;height:60px}

/* services */
.services{position:absolute;left:0;top:1167px;width:1200px;height:380px;display:flex}
.service{width:400px;height:380px;position:relative;background:var(--black);text-align:center;color:var(--white)}
.service.featured{background:var(--grad)}
.service svg.icon{position:absolute;left:146px;top:52px}
.service h3{position:absolute;left:0;top:183px;width:380px;font-family:'Montserrat',sans-serif;font-weight:700;font-size:16px;line-height:23px;text-transform:uppercase}
.service p{position:absolute;left:40px;top:247px;width:300px;font-size:13.5px;line-height:27px;color:#dddddd}
.service.featured p{color:#f1c6c2}
.service svg.more{position:absolute;left:168px;top:318px}

/* testimonials */
.section-title{position:absolute;left:0;top:1605px;width:1200px;text-align:center;font-size:42px}
.quote-card{position:absolute;left:273px;top:1715px;width:654px;height:174px;background:var(--white);border-radius:8px;box-shadow:0 2px 14px rgba(0,0,0,.12)}
.quote-card p{position:absolute;left:50px;top:48px;width:554px;text-align:center;font-size:13.5px;line-height:29px;color:var(--text)}
.client-name{position:absolute;left:0;top:1928px;width:1200px;text-align:center;font-family:'Montserrat',sans-serif;font-weight:600;font-size:20px;color:#222}
.client-site{position:absolute;left:0;top:1953px;width:1200px;text-align:center;font-size:13px;color:var(--red)}
.btn-feedback{left:478px;top:1999px;width:244px;height:52px;font-size:20px}

/* call to action */
.cta{position:absolute;left:0;top:2115px;width:1200px;height:406px;background:var(--grad)}
.cta-title{position:absolute;left:77px;top:2185px;font-size:42px;line-height:47px;color:#1a0b0b}
.cta-copy{position:absolute;left:79px;top:2298px;width:560px;font-size:13.5px;line-height:27px;color:var(--white)}
.btn-start{left:79px;top:2399px;width:206px;height:51px;font-size:20px;background:transparent;border:2px solid var(--white)}
.device{position:absolute;left:806px;top:2068px;width:264px;height:518px;background:var(--white);border:2px solid #d8d0c8;border-radius:34px;box-shadow:0 6px 14px rgba(0,0,0,.12)}
.device-screen{position:absolute;left:10px;top:40px;width:240px;height:422px;border:1px solid #e5e5e5}
.device-brand{position:absolute;left:0;top:90px;width:100%;text-align:center;font-family:'Montserrat',sans-serif;font-weight:700;font-size:31px;color:var(--ink)}
.device-label{position:absolute;left:0;top:154px;width:100%;text-align:center;font-size:16px;color:var(--red)}
.field{position:absolute;left:22px;width:198px;height:46px;border:1px solid #dddddd;padding:0 15px;display:flex;align-items:center;font-size:13px;color:#777}
.btn-device{left:76px;top:307px;width:94px;height:41px;font-size:15px}

/* footer */
.footer-brand{position:absolute;left:121px;top:2658px;font-family:'Montserrat',sans-serif;font-weight:700;font-size:38px;color:var(--ink)}
.social{position:absolute;top:2713px;width:42px;height:42px;border-radius:50%}
.footer-head{position:absolute;top:2628px;font-family:'Montserrat',sans-serif;font-weight:700;font-size:16px;color:#222;text-transform:uppercase}
.footer-list{position:absolute;list-style:none}
.footer-list li{position:relative;height:31.3px;padding-left:21px;font-size:13.5px;color:#555}
.footer-list li::before{content:"";position:absolute;left:0;top:8px;width:5px;height:5px;border-radius:50%;background:var(--red)}
.contact-line{position:absolute;left:886px;display:flex;align-items:center;gap:13px;font-size:13.5px;color:#444}
.footer-rule{position:absolute;left:77px;top:2829px;width:1045px;height:1px;background:var(--line)}
.copyright{position:absolute;left:0;top:2849px;width:1200px;text-align:center;font-size:13.5px;color:#555}
</style>
</head>
<body>

<header class="site-header">
  <div class="brand">Tarvolin</div>
  <span class="nav active" style="left:730px">Home</span>
  <span class="nav" style="left:805px">About Us</span>
  <span class="nav" style="left:908px">Contact Us</span>
  <div class="btn btn-login">Login</div>
</header>

<section class="hero" role="img" aria-label="Photo of a team working together at a laptop">
  <div class="slider-arrow" style="left:14px"><svg width="48" height="48" viewBox="0 0 48 48"><path d="M27 15 L18 24 L27 33" fill="none" stroke="#fff" stroke-width="1.5"/></svg></div>
  <div class="slider-arrow" style="left:1138px"><svg width="48" height="48" viewBox="0 0 48 48"><path d="M21 15 L30 24 L21 33" fill="none" stroke="#fff" stroke-width="1.5"/></svg></div>
  <h1 class="hero-title">Automating customs clearance<br>processes software</h1>
  <p class="hero-sub">With intelligent/smart/digital Customs Clearance Software</p>
  <div class="btn btn-hero">Contact Us</div>
</section>

<section>
  <h2 class="heading welcome-title">Welcome to<br><span class="accent">Tarvolin</span></h2>
  <p class="welcome-copy" style="top:849px">Lorem Ipsum is simply dummy text of the printing and typesetting industry. Lorem Ipsum has been the industry's standard dummy text ever since the.</p>
  <p class="welcome-copy" style="top:919px">Lorem Ipsum is simply dummy text of the printing and typesetting industry. Lorem Ipsum has been the industry's standard dummy text ever since the 1500s, when an unknown printer took a galley of type and scrambled it. Lorem Ipsum is simply dummy text of the printing.</p>
  <div class="btn btn-learn">Learn More</div>
  <div class="welcome-frame"></div>
  <div class="welcome-media" role="img" aria-label="Video still: a person facing a robot in front of digital code"></div>
  <svg class="play" viewBox="0 0 60 60"><circle cx="30" cy="30" r="30" fill="#fff"/><circle cx="30" cy="30" r="25" fill="var(--red)"/><path d="M25 21 L38 30 L25 39 Z" fill="#fff"/></svg>
</section>

<section class="services">
  <article class="service">
    <svg class="icon" width="108" height="108" viewBox="0 0 108 108"><circle cx="54" cy="54" r="53" fill="none" stroke="var(--red)" stroke-width="1.5"/><rect x="25" y="26" width="48" height="44" fill="none" stroke="var(--red)" stroke-width="2"/><line x1="25" y1="34" x2="73" y2="34" stroke="var(--red)" stroke-width="2"/><rect x="31" y="40" width="16" height="10" fill="none" stroke="var(--red)" stroke-width="2"/><rect x="50" y="50" width="33" height="28" fill="none" stroke="var(--red)" stroke-width="2"/><line x1="55" y1="58" x2="78" y2="58" stroke="var(--red)" stroke-width="2"/><line x1="55" y1="64" x2="78" y2="64" stroke="var(--red)" stroke-width="2"/><line x1="55" y1="70" x2="78" y2="70" stroke="var(--red)" stroke-width="2"/></svg>
    <h3>Applying a Web<br>Application</h3>
    <p>Lorem Ipsum is simply dummy text of the printing and typesetting industry.</p>
    <svg class="more" width="42" height="12" viewBox="0 0 42 12"><path d="M0 6 H40 M34 1 L40 6 L34 11" fill="none" stroke="var(--red)" stroke-width="1.3"/></svg>
  </article>
  <article class="service featured">
    <svg class="icon" width="108" height="108" viewBox="0 0 108 108"><circle cx="54" cy="54" r="53" fill="none" stroke="#fff" stroke-width="1.5"/><rect x="40" y="25" width="28" height="20" rx="4" fill="none" stroke="#fff" stroke-width="2"/><circle cx="48" cy="34" r="3" fill="none" stroke="#fff" stroke-width="2"/><circle cx="60" cy="34" r="3" fill="none" stroke="#fff" stroke-width="2"/><rect x="38" y="49" width="32" height="24" rx="3" fill="none" stroke="#fff" stroke-width="2"/><path d="M38 55 H28 V48 M70 55 H80 V64" fill="none" stroke="#fff" stroke-width="2"/><rect x="42" y="75" width="9" height="10" fill="none" stroke="#fff" stroke-width="2"/><rect x="57" y="75" width="9" height="10" fill="none" stroke="#fff" stroke-width="2"/></svg>
    <h3>Artificial<br>Intelligence</h3>
    <p>Lorem Ipsum is simply dummy text of the printing and typesetting industry.</p>
    <svg class="more" width="42" height="12" viewBox="0 0 42 12"><path d="M0 6 H40 M34 1 L40 6 L34 11" fill="none" stroke="#fff" stroke-width="1.3"/></svg>
  </article>
  <article class="service">
    <svg class="icon" width="108" height="108" viewBox="0 0 108 108"><circle cx="54" cy="54" r="53" fill="none" stroke="var(--red)" stroke-width="1.5"/><rect x="26" y="76" width="22" height="8" fill="none" stroke="var(--red)" stroke-width="2"/><path d="M33 76 V58 L50 34 L74 36" fill="none" stroke="var(--red)" stroke-width="2"/><circle cx="35" cy="58" r="5" fill="none" stroke="var(--red)" stroke-width="2"/><circle cx="50" cy="34" r="6" fill="none" stroke="var(--red)" stroke-width="2"/><circle cx="74" cy="36" r="5" fill="none" stroke="var(--red)" stroke-width="2"/><path d="M74 41 V50 M70 54 L74 50 L78 54" fill="none" stroke="var(--red)" stroke-width="2"/></svg>
    <h3>Robotic Process<br>Automation</h3>
    <p>Lorem Ipsum is simply dummy text of the printing and typesetting industry.</p>
    <svg class="more" width="42" height="12" viewBox="0 0 42 12"><path d="M0 6 H40 M34 1 L40 6 L34 11" fill="none" stroke="var(--red)" stroke-width="1.3"/></svg>
  </article>
</section>

<section>
  <h2 class="heading section-title">What our <span class="accent">client say</span></h2>
  <div class="quote-card">
    <p>Lorem Ipsum is simply dummy text of the printing and typesetting industry. Lorem Ipsum has been the industry's standard dummy text ever since the 1500s, when an unknown printer took a galley of type and scrambled it.</p>
  </div>
  <svg class="abs" style="left:307px;top:1700px" width="38" height="34" viewBox="0 0 38 34"><path d="M2 34 V18 L10 0 H16 L11 16 H16 V34 Z M21 34 V18 L29 0 H35 L30 16 H35 V34 Z" fill="var(--red)"/></svg>
  <svg class="abs" style="left:859px;top:1872px" width="38" height="34" viewBox="0 0 38 34"><path d="M36 0 V16 L28 34 H22 L27 18 H22 V0 Z M17 0 V16 L9 34 H3 L8 18 H3 V0 Z" fill="var(--red)"/></svg>
  <div class="client-name">CLIENT NAME</div>
  <div class="client-site">something.com</div>
  <div class="btn btn-feedback">Leave Feedback</div>
</section>

<section class="cta"></section>
<h2 class="heading cta-title">Ready to<br>get started</h2>
<p class="cta-copy">Lorem Ipsum is simply dummy text of the printing and typesetting industry. Lorem Ipsum has been the industry's standard dummy text ever since the 1500s, when an unknown printer took a galley of type and scrambled it.</p>
<div class="btn btn-start">Get Started</div>

<div class="device">
  <svg class="abs" style="left:40px;top:14px" width="180" height="12" viewBox="0 0 180 12"><rect x="0" y="4" width="14" height="3" rx="1.5" fill="#bbb"/><rect x="62" y="4" width="52" height="4" rx="2" fill="#333"/><circle cx="120" cy="6" r="5" fill="#999"/><circle cx="138" cy="6" r="4" fill="#ccc"/></svg>
  <div class="device-screen">
    <div class="device-brand">Tarvolin</div>
    <div class="device-label">Login</div>
    <div class="field" style="top:193px">Enter Name *</div>
    <div class="field" style="top:247px">Enter Email *</div>
    <div class="btn btn-device">Login</div>
  </div>
  <svg class="abs" style="left:40px;top:484px" width="180" height="14" viewBox="0 0 180 14"><path d="M0 5 H16 M2 8 H16" stroke="#bbb" stroke-width="1.2"/><path d="M80 10 A10 8 0 0 1 98 10 Z" fill="none" stroke="#bbb" stroke-width="1.2"/><path d="M164 4 H176 V10 H162 M166 7 L162 10 L166 13" fill="none" stroke="#bbb" stroke-width="1.2"/></svg>
</div>

<footer>
  <div class="footer-brand">Tarvolin</div>
  <div class="social" style="left:117px;background:#3b5998" role="img" aria-label="Social link"></div>
  <div class="social" style="left:163px;background:#1da1f2" role="img" aria-label="Social link"></div>
  <div class="social" style="left:209px;background:#0e6aa8" role="img" aria-label="Social link"></div>
  <div class="social" style="left:253px;background:#cc2e2e" role="img" aria-label="Social link"></div>

  <div class="footer-head" style="left:347px">Sitemap</div>
  <ul class="footer-list" style="left:346px;top:2676px"><li>Home</li><li>About Us</li><li>Contact Us</li></ul>

  <div class="footer-head" style="left:613px">Quick Link</div>
  <ul class="footer-list" style="left:612px;top:2676px"><li>Terms Of Use</li><li>Terms Of App</li><li>Privacy Policy</li><li>Terms of Conditions</li></ul>

  <div class="footer-head" style="left:878px">Get in Touch</div>
  <div class="contact-line" style="top:2679px"><svg width="20" height="20" viewBox="0 0 24 24"><path d="M6.6 10.8a15 15 0 0 0 6.6 6.6l2.2-2.2c.3-.3.7-.4 1-.2 1.1.4 2.3.6 3.6.6.6 0 1 .4 1 1V20c0 .6-.4 1-1 1A17 17 0 0 1 3 4c0-.6.4-1 1-1h3.5c.6 0 1 .4 1 1 0 1.3.2 2.5.6 3.6.1.3 0 .7-.2 1z" fill="var(--red)"/></svg>123 456 7890</div>
  <div class="contact-line" style="top:2715px"><svg width="20" height="20" viewBox="0 0 24 24"><rect x="2" y="5" width="20" height="14" fill="var(--red)"/><path d="M2 5 L12 13 L22 5" fill="none" stroke="#fff" stroke-width="1.5"/></svg>info@tarvolin-example.com</div>

  <div class="footer-rule"></div>
  <div class="copyright">©Tarvolin - 2019 All Right reserved.</div>
</footer>

</body>
</html>
```